IT COMPANYcutting edge tec business card

we are IT company that building any apps.
we need business card in japanese and english
You don’t have to include all information in front one you can attach part of that information to back-side
company name : 株式会社ひかりの丘 (BRIGHTHILL Inc.)
concept : cutting-edge technology
role : 取締役 (director)
name : 呉 炫秀 (Oh Hyeonsuk)
post number : 154-0038
address : 東京都世田谷区西若葉台5-14-8 (5-14-8, Nishiwakabadai, Setagaya Ku, Tokyo To, 154-0038, Japan)
Tel:+81-3-5917-2846
Mobile:+81-80-7253-3169
Email : hoh@brighthill-lab.com
website : www.brighthill-lab.com

we dont have logo so please make it as well
we also looking for designer who can make homapage design.

Contact Information for Business Card

cutting-edge design and modern for IT

Font styles to use
Sans Serif

Colors
34a6d7
33b8a4
6092c4
3377b5
886aae
6b449b
b868aa
a64599

Requirements
Must have
• Simple but designed

```html
<!DOCTYPE html>
<html lang="en">
<head>
<meta charset="utf-8">
<title>BRIGHTHILL Inc. — Business Card</title>
<link rel="stylesheet" href="https://fonts.googleapis.com/css2?family=Lato:wght@400;700;900&display=swap">
<style>
  :root {
    --navy: #0f2d52;
    --navy-deep: #0b2546;
    --navy-tile: #1e3f6b;
    --ink-grey: #58595c;
    --text: #1d1d1f;
    --bar-grey: #e6e8eb;
    --square-grey: #6a6b6e;
    --page: #2a2a2c;
    --card: #ffffff;
  }
  * { box-sizing: border-box; margin: 0; padding: 0; }
  html, body { width: 1200px; height: 878px; overflow: hidden; }
  body {
    background: var(--page);
    font-family: "Lato", sans-serif;
    display: flex;
    flex-direction: column;
    align-items: center;
    justify-content: center;
    gap: 36px;
  }
  .card {
    position: relative;
    width: 660px;
    height: 384px;
    overflow: hidden;
    box-shadow: 0 10px 28px rgba(0,0,0,.45);
  }

  /* Back */
  .card-back { background: var(--navy-deep); }
  .back-pattern {
    position: absolute; inset: 0;
    background: linear-gradient(135deg, var(--navy-tile), var(--navy-deep));
  }
  .back-wordmark {
    position: absolute;
    right: 60px; top: 120px;
    color: #ffffff;
    font-weight: 700;
    font-size: 30px;
    letter-spacing: 1px;
  }

  /* Front */
  .card-front { background: var(--card); }
  .wordmark {
    position: absolute; left: 40px; top: 36px;
    color: var(--ink-grey);
    font-weight: 700;
    font-size: 36px;
    letter-spacing: 1.5px;
  }
  .holder { position: absolute; left: 40px; top: 106px; }
  .holder-name { color: var(--navy); font-weight: 900; font-size: 29px; line-height: 1.1; }
  .holder-role { color: var(--ink-grey); font-size: 15px; margin-top: 2px; }
  .address {
    position: absolute; left: 40px; top: 182px;
    color: var(--text); font-size: 15.5px; line-height: 1.3; width: 360px;
  }
  .contacts {
    position: absolute; left: 40px; top: 244px;
    list-style: none; color: var(--text); font-size: 16px;
  }
  .contacts li { display: flex; align-items: center; gap: 12px; height: 24px; }
  .contacts svg { width: 16px; height: 16px; fill: var(--navy); flex: none; }
  .placeholder-bar {
    position: absolute; right: 36px; width: 236px; height: 44px;
    background: var(--bar-grey);
  }
  .bar-1 { top: 112px; }
  .bar-2 { top: 212px; }
  .bar-3 { top: 312px; }
  .corner-square {
    position: absolute; left: 0; bottom: 0;
    width: 50px; height: 20px; background: var(--square-grey);
  }
  .base-band {
    position: absolute; left: 58px; right: 0; bottom: 0;
    height: 14px; background: var(--navy);
  }
</style>
</head>
<body>
  <section class="card card-back" aria-label="Card back">
    <div class="back-pattern" role="img" aria-label="Navy tiled pattern of short diagonal bars"></div>
    <div class="back-wordmark">BRIGHTHILL Inc.</div>
  </section>

  <section class="card card-front" aria-label="Card front">
    <div class="wordmark">BRIGHTHILL Inc.</div>
    <div class="holder">
      <div class="holder-name">Oh Hyeonsuk</div>
      <div class="holder-role">Director</div>
    </div>
    <p class="address">5-14-8, Nishiwakabadai, Setagaya Ku, Tokyo To, 154-0038, Japan</p>
    <ul class="contacts">
      <li><svg viewBox="0 0 16 16"><path d="M2 6c0-2 3-3 6-3s6 1 6 3v1h-3V6H5v1H2zM4 8h8l1 5H3z"/></svg>+81-3-5917-2846</li>
      <li><svg viewBox="0 0 16 16"><path d="M4 1h8v14H4zM5.5 2.5v9h5v-9zM7 13h2v1H7z" fill-rule="evenodd"/></svg>+81-80-7253-3169</li>
      <li><svg viewBox="0 0 16 16"><path d="M1 3h14v10H1zM2 4l6 5 6-5z" fill-rule="evenodd"/></svg>hoh@brighthill-lab.com</li>
      <li><svg viewBox="0 0 16 16"><circle cx="8" cy="8" r="6.5" fill="none" stroke="#0f2d52" stroke-width="1.3"/><path d="M1.5 8h13M8 1.5v13" stroke="#0f2d52" stroke-width="1"/></svg>www.brighthill-lab.com</li>
    </ul>
    <div class="placeholder-bar bar-1"></div>
    <div class="placeholder-bar bar-2"></div>
    <div class="placeholder-bar bar-3"></div>
    <div class="corner-square"></div>
    <div class="base-band"></div>
  </section>
</body>
</html>
```